Brand-new Pediatric Dental Practice needs a website

We are a brand-new dental practice that will specialize in treating children. We want a gorgeous and easily navigable dental practice website that would make a good first impression to potential patients and their parents. It should be modern, SEO-friendly, mobile responsive, and optimized to win new patients.

Target Market(s)

Parents

Industry/Entity Type

Healthcare/Dentistry

Coding

Coded - Design and coding required

Number of Pages Required

4 page

Requirements
Must have
• Use the Wix website building platform. 4 pages: home, meet our dentists, services, contact us
Nice to have
• has a link to our facebook, instagram

```html
<!DOCTYPE html>
<html lang="en">
<head>
<meta charset="utf-8">
<title>Birchwood Pediatric Dentistry</title>
<link href="https://fonts.googleapis.com/css2?family=Poppins:ital,wght@0,400;0,500;0,600;0,700;1,400&display=swap" rel="stylesheet">
<style>
:root{
  --green:#3d9a54;
  --green-dark:#2f8a46;
  --green-card:#5dbb72;
  --green-soft:#6fc583;
  --mint:#eefaee;
  --mint-2:#e3f6e3;
  --topbar:#a9dca6;
  --ink:#1a1a1a;
  --text:#444;
  --line:#e3e3e3;
  --white:#fff;
  --footer:#161616;
  --star:#f5b400;
}
*{box-sizing:border-box;margin:0;padding:0}
html,body{width:1200px;height:4971px;overflow:hidden}
body{font-family:'Poppins',sans-serif;color:var(--text);background:var(--white);position:relative}
section,header,footer{position:relative;width:1200px}
.abs{position:absolute}
h2.section-title{font-size:34px;font-weight:700;color:var(--ink);text-align:center;position:absolute;left:0;width:1200px}
.title-rule{position:absolute;left:575px;width:50px;height:3px;background:var(--green);border-radius:2px}
.lead{position:absolute;left:160px;width:880px;text-align:center;font-size:14px;line-height:29px;color:var(--text)}
.btn{display:inline-flex;align-items:center;gap:6px;border-radius:30px;font-weight:600;font-size:13px;text-transform:uppercase;letter-spacing:.2px;white-space:nowrap}
.arr{display:inline-block;width:13px;height:13px;border-radius:50%;background:currentColor;position:relative;flex:none}
.arr::after{content:"";position:absolute;left:4px;top:3.5px;width:0;height:0;border-left:6px solid var(--white);border-top:3px solid transparent;border-bottom:3px solid transparent}
.btn-green{background:var(--green-dark);color:var(--white);padding:0 28px;height:48px}
.btn-green .arr::after{border-left-color:var(--green-dark)}
.btn-white{background:var(--white);color:var(--green-dark);padding:0 30px;height:44px}
.photo{position:absolute;border-radius:50%}

.topbar{height:37px;background:var(--topbar);font-size:12px;color:#2b4b2e;display:flex;align-items:center;justify-content:center}
.topbar b{text-decoration:underline;margin-left:4px}
.site-header{height:108px;background:var(--white)}
.brand{position:absolute;left:100px;top:14px;display:flex;align-items:center;gap:10px}
.brand-dot{width:34px;height:34px;border-radius:50%;background:var(--green-soft)}
.brand-name{font-size:22px;font-weight:500;color:#555;line-height:1}
.contact-line{position:absolute;right:120px;top:20px;display:flex;align-items:center;gap:14px;font-size:15px;font-weight:500;color:#222;white-space:nowrap}
.contact-line svg{vertical-align:-2px;margin-right:4px}
.soc{width:30px;height:30px;border-radius:50%;border:1.5px solid var(--green-soft)}
.soc-row{display:flex;gap:8px}
.nav{position:absolute;left:0;top:63px;width:1200px;height:45px;border-top:1px solid var(--line);background:#fafafa;display:flex;align-items:center;padding-left:378px;gap:54px;font-size:13px;font-weight:600;color:#222}

.hero{height:646px;background:linear-gradient(90deg,#eceeee 0%,#e6e8e8 45%,#dcdfdf 100%);overflow:hidden}
.hero-photo{position:absolute;left:540px;top:0;width:660px;height:646px;background:radial-gradient(ellipse at 55% 45%,#e9cbb7 0%,#c9a994 30%,#d9dcdc 62%,#dfe1e1 100%)}
.hero h1{position:absolute;left:100px;top:190px;font-size:45px;line-height:48px;font-weight:700;color:var(--ink)}
.hero p{position:absolute;left:100px;top:290px;width:440px;font-size:15px;line-height:31px;color:#333;font-weight:500}
.hero .btn{position:absolute;left:100px;top:374px}
.hero-arrow{position:absolute;top:320px}
.dots{position:absolute;left:540px;top:594px;width:120px;height:28px;border-radius:14px;background:rgba(60,60,60,.45);display:flex;align-items:center;justify-content:center;gap:8px}
.dots i{width:14px;height:14px;border-radius:50%;border:2px solid var(--white)}
.dots i.on{background:var(--white)}

.welcome{height:781px}
.deco{position:absolute}
.card{position:absolute;top:300px;width:320px;height:372px;background:var(--green-card);border-radius:6px;color:var(--white);text-align:center;box-shadow:0 4px 10px rgba(0,0,0,.08)}
.card.alt{background:var(--green)}
.card .ring{position:absolute;left:60px;top:-36px;width:200px;height:200px;border-radius:50%;background:var(--white);padding:8px}
.card .ring div{width:100%;height:100%;border-radius:50%}
.card h3{position:absolute;top:208px;width:100%;font-size:22px;font-weight:500;white-space:nowrap}
.card p{position:absolute;top:254px;left:25px;width:270px;font-size:13px;line-height:27px;color:#eaf7ec}
.card .btn-wrap{position:absolute;top:340px;left:0;width:100%;display:flex;justify-content:center}
.card .btn-white{height:42px;padding:0 30px;font-size:12.5px}

.about{height:598px;background:var(--mint)}
.about h2{position:absolute;left:110px;top:88px;font-size:36px;font-weight:700;color:var(--ink)}
.about .rule{position:absolute;left:110px;top:142px;width:50px;height:3px;background:var(--green)}
.about p{position:absolute;left:110px;top:162px;width:470px;font-size:12.5px;line-height:22.5px;color:#444}
.about .btn{position:absolute;left:114px;top:474px}
.about-ring{position:absolute;left:636px;top:72px;width:454px;height:454px;border-radius:50%;border:3px solid var(--green);background:var(--white)}
.about-ring .photo{left:14px;top:14px;width:420px;height:420px;background:radial-gradient(circle at 50% 40%,#e8c4ae 0%,#b88f7a 30%,#7d97a9 60%,#5b6e7d 100%)}

.services{height:679px}
.svc{position:absolute;top:240px;width:320px;text-align:center}
.svc .icon{width:112px;height:112px;border-radius:50%;background:var(--mint-2);margin:0 auto}
.svc h3{margin-top:32px;font-size:21px;font-weight:500;color:var(--ink);white-space:nowrap}
.svc p{margin-top:10px;font-size:13px;line-height:29px;color:#555}
.svc .more{display:inline-flex;margin-top:14px;font-size:13px;font-weight:600;color:var(--green-dark);border-bottom:2px solid var(--green-dark);gap:5px;align-items:center;text-transform:uppercase;white-space:nowrap}

.team{height:691px;background:var(--mint)}
.team .portrait{position:absolute;left:168px;top:262px;width:342px;height:342px;background:radial-gradient(circle at 50% 40%,#d9b39c 0%,#a98876 25%,#e8eef2 55%,#cfd9e0 100%)}
.team h3{position:absolute;left:571px;top:286px;font-size:28px;font-weight:500;color:var(--ink);white-space:nowrap}
.team .role{position:absolute;left:571px;top:331px;font-size:13px;font-weight:500;color:#222;letter-spacing:.5px}
.team p.bio{position:absolute;left:571px;top:362px;width:470px;font-size:12.5px;line-height:28px;color:#444}
.team .btn{position:absolute;left:573px;top:548px}
.circle-arrow{position:absolute;top:408px;width:50px;height:50px;border-radius:50%;border:1.5px solid #333}

.patients{height:511px}
.review{position:absolute;top:182px;width:320px}
.review p{margin-top:10px;font-size:16px;line-height:28.5px;font-style:italic;color:#333}
.who{display:flex;align-items:center;gap:14px;margin-top:20px;font-size:15px;font-weight:600;color:#222}
.who span.av{width:52px;height:52px;border-radius:50%;background:radial-gradient(circle,#c9a590 0%,#8f8d8f 60%,#d8d8d8 100%);border:2px solid var(--white);box-shadow:0 0 0 1px var(--line)}

.contact{height:549px;background:var(--mint-2);overflow:hidden}
.map{position:absolute;left:100px;top:83px;width:315px;height:315px;background:linear-gradient(135deg,#eceeed 0%,#dfe2e1 50%,#e8eae9 100%)}
.contact .soc-row{position:absolute;left:100px;top:422px}
.info{position:absolute;left:440px;top:83px;width:316px;height:380px;background:var(--white);padding:20px 10px 0 10px;font-size:12.5px;color:#222}
.info h4{font-size:12.5px;font-weight:600;padding-bottom:8px;border-bottom:1px solid var(--line);margin-bottom:8px}
.info .val{margin-bottom:24px;display:flex;align-items:center;gap:4px;white-space:nowrap}
.hours{width:100%;border-collapse:collapse;font-size:12px}
.hours td{padding:6px 0;border-bottom:1px solid var(--line)}
.hours td:last-child{padding-left:40px}
.form{position:absolute;left:781px;top:83px;width:320px}
.field{height:42px;background:var(--white);border:1px solid #dcdcdc;margin-bottom:11px;font-size:12.5px;color:#555;padding:10px 12px}
.field.msg{height:96px}
.form .btn{margin-top:12px;height:46px;padding:0 52px}

.site-footer{height:371px;background:var(--footer);color:var(--white);text-align:center}
.foot-brand{position:absolute;left:0;top:86px;width:1200px;display:flex;flex-direction:column;align-items:center;gap:12px}
.foot-brand .brand-dot{width:70px;height:70px;background:var(--white)}
.foot-brand .brand-name{color:var(--white);font-size:34px;font-weight:400}
.foot-nav{position:absolute;left:0;top:210px;width:1200px;display:flex;justify-content:center;font-size:15px}
.foot-nav span{padding:0 42px}
.foot-nav i{font-style:normal}
.copy{position:absolute;left:0;top:256px;width:1200px;font-size:13px}
.foot-soc{position:absolute;left:0;top:300px;width:1200px;display:flex;justify-content:center;gap:10px}
.foot-soc span{width:38px;height:38px;border-radius:50%;background:var(--white)}
</style>
</head>
<body>

<div class="topbar">Masks/Face coverings required.&nbsp; See our current <b>COVID-19 Protocols</b></div>

<header class="site-header">
  <div class="brand"><span class="brand-dot"></span><span class="brand-name">birchwood</span></div>
  <div class="contact-line">
    <span><svg width="14" height="14" viewBox="0 0 24 24"><rect x="1" y="1" width="22" height="22" rx="4" fill="#3d9a54"/><path d="M8 5c1 0 2 3 2 4s-2 1-1 3 2 3 3 3 1-1 2-1 4 1 4 2-1 3-3 3C10 19 5 14 5 8c0-2 2-3 3-3z" fill="#fff"/></svg>+1 555-010-2040</span>
    <span><svg width="16" height="13" viewBox="0 0 16 13"><rect width="16" height="13" rx="1.5" fill="#3d9a54"/><path d="M1 2l7 5 7-5" stroke="#fff" stroke-width="1.6" fill="none"/></svg>hello@birchwoodkidsdental.com</span>
    <span class="soc-row"><span class="soc"></span><span class="soc"></span><span class="soc"></span></span>
  </div>
  <nav class="nav"><span>HOME</span><span>ABOUT US</span><span>NEW PATIENTS</span><span>DENTISTRY</span><span>FORMS</span><span>CONTACT US</span></nav>
</header>

<section class="hero">
  <div class="hero-photo" role="img" aria-label="Photo of a smiling young child"></div>
  <h1>Birchwood<br>Pediatric Dentistry</h1>
  <p>Sed ut perspiciatis unde omnis iste r sit voluptatem accusantium doloremque laudantium</p>
  <span class="btn btn-green">Book an appointment <span class="arr"></span></span>
  <svg class="hero-arrow" style="left:60px" width="24" height="44" viewBox="0 0 24 44"><path d="M22 2L2 22l20 20" stroke="#fff" stroke-width="2" fill="none"/></svg>
  <svg class="hero-arrow" style="left:1118px" width="24" height="44" viewBox="0 0 24 44"><path d="M2 2l20 20L2 42" stroke="#fff" stroke-width="2" fill="none"/></svg>
  <div class="dots"><i></i><i class="on"></i><i></i><i></i></div>
</section>

<section class="welcome">
  <div class="deco" role="img" aria-label="Illustration of a cartoon butterfly" style="left:1050px;top:20px;width:150px;height:110px;border-radius:50%;background:radial-gradient(circle,#f6b660 0%,#ec8b5a 55%,rgba(255,255,255,0) 72%)"></div>
  <h2 class="section-title" style="top:86px;font-size:30px">Welcome To Birchwood Pediatric Dentistry</h2>
  <p class="lead" style="top:150px;left:130px;width:940px">Sed ut perspiciatis unde omnis iste natus error sit voluptatem accusantium doloremque laudantium, totam rem aperiam, eaque ipsa quae ab illo inventore veritatis et quasi architecto beatae vitae dicta sunt exbo. Nemo enim ipsam voluptatem quia voluptas sit aspernatur aut odit aut fugit, sed quia consequuntur</p>

  <div class="card" style="left:100px">
    <div class="ring"><div role="img" aria-label="Photo of a dental treatment room" style="background:radial-gradient(circle,#f2f4f6 0%,#c7d0d8 60%,#8e9aa6 100%)"></div></div>
    <h3>Clinic Tour</h3>
    <p>Sed ut perspiciatis undemnis iste natr sit volupem accusantium doloremque laudantium, totam</p>
    <div class="btn-wrap"><span class="btn btn-white">Learn more <span class="arr"></span></span></div>
  </div>
  <div class="card alt" style="left:440px">
    <div class="ring"><div role="img" aria-label="Photo of a dentist examining a child" style="background:radial-gradient(circle,#e5c6b2 0%,#9cb3c7 55%,#6f8aa1 100%)"></div></div>
    <h3>Family Resources</h3>
    <p>Sed ut perspiciatis undemnis iste natr sit volupem accusantium doloremque laudantium, totam</p>
    <div class="btn-wrap"><span class="btn btn-white">Learn more <span class="arr"></span></span></div>
  </div>
  <div class="card" style="left:779px">
    <div class="ring"><div role="img" aria-label="Photo of the clinic reception area" style="background:radial-gradient(circle,#d9d2c6 0%,#8c7e6e 55%,#4e4a46 100%)"></div></div>
    <h3>Finding Your Way Around</h3>
    <p>Sed ut perspiciatis undemnis iste natr sit volupem accusantium doloremque laudantium, totam</p>
    <div class="btn-wrap"><span class="btn btn-white">Learn more <span class="arr"></span></span></div>
  </div>
</section>

<section class="about">
  <h2>About Us</h2>
  <div class="rule"></div>
  <p>At vero eos et accusamus et iusto odio dignissimos ducimus i blanditiis praesentium voluptatum deleniti atque i quos dolores et quas molestias excepturi sint occaecati cupiditate no provident, similique sunt in culpa qui officia deserunt mollitia animi, id laborum et dolorum fuga. Et harum quidem rerum facilis est et expedita distincio. Nam libero tempore, cum soluta nobis est eligendi optio cumque nihil impedit quo minus id quod maxime placeat facere posmus, omnis voluptas assumenda est, omnis dolor repellendus. Temporibus aut quibusdam et aut officiis debitis aut rerum necessitatibus saepe eveniet ut et voluptates repudiandae sint et molestiae non recusandae.</p>
  <span class="btn btn-green">Learn more <span class="arr"></span></span>
  <div class="about-ring"><div class="photo" role="img" aria-label="Photo of a smiling girl at a dental checkup"></div></div>
</section>

<section class="services">
  <div class="deco" role="img" aria-label="Illustration of a bird on a leafy branch" style="left:0;top:10px;width:235px;height:200px;background:radial-gradient(ellipse at 40% 55%,#a7d37b 0%,#c7e2a8 40%,rgba(255,255,255,0) 70%)"></div>
  <h2 class="section-title" style="top:80px">Our services</h2>
  <div class="title-rule" style="top:134px"></div>
  <p class="lead" style="top:148px;left:150px;width:900px">Sed ut perspiciatis unde omnis iste natus error sit voluptatem accusantium doloremque laudantium, totam rem aperiam, eaque ipsa quae ab illo inventore veritatis et quasi architecto</p>

  <div class="svc" style="left:93px"><div class="icon" role="img" aria-label="Tooth illustration"></div><h3>Sedation Dentistry</h3><p>Sed ut perspiciatis unde omnis iste natus&nbsp; sit volm accusantium doloremque laudantium, totam rem aperiam, eaque ipsa quae ab illo inventore veritati</p><span class="more">Learn more <span class="arr"></span></span></div>
  <div class="svc" style="left:440px"><div class="icon" role="img" aria-label="Tooth with plus sign illustration"></div><h3>Pediatric Hospital Dentistry</h3><p>Sed ut perspiciatis unde omnis iste natus&nbsp; sit volm accusantium doloremque laudantium, totam rem aperiam, eaque ipsa quae ab illo inventore veritati</p><span class="more">Learn more <span class="arr"></span></span></div>
  <div class="svc" style="left:785px"><div class="icon" role="img" aria-label="Tooth with heart illustration"></div><h3>Pediatric Dentistry</h3><p>Sed ut perspiciatis unde omnis iste natus&nbsp; sit volm accusantium doloremque laudantium, totam rem aperiam, eaque ipsa quae ab illo inventore veritati</p><span class="more">Learn more <span class="arr"></span></span></div>
</section>

<section class="team">
  <h2 class="section-title" style="top:70px">Meet Our Team</h2>
  <div class="title-rule" style="top:124px"></div>
  <p class="lead" style="top:136px">Sed ut perspiciatis unde omnis iste natus error sit voluptatem accusantium doloremque laudantium, totam rem aperiam, eaque ipsa quae ab illo inventore veritatis et quasi architecto beatae vitae dicta sunt exbo. Nemo enim ipsam voluptatem quia voluptas sit aspernatur aut odit aut fugit, sed quia consequuntur</p>
  <div class="circle-arrow" style="left:87px"><svg width="47" height="47" viewBox="0 0 50 50"><path d="M28 16l-9 9 9 9" stroke="#333" stroke-width="2" fill="none"/></svg></div>
  <div class="photo portrait" role="img" aria-label="Portrait of the dentist in a white coat"></div>
  <h3>Daniel Marlowe, DDS</h3>
  <div class="role">GENERAL DENTIST</div>
  <p class="bio">At vero eos et accusamus et iusto odio dignissimos ducimus i blanditiis praesentium voluptatum deleniti atque i quos dolores et quas molestias excepturi sint occaecati cupiditate no provident, similique sunt in culpa qui officia deserunt mollitia animi, id laborum et dolorum fuga. Et harum quidem rerum facilis est et expedita distincio.</p>
  <span class="btn btn-green">Learn more <span class="arr"></span></span>
  <div class="circle-arrow" style="left:1062px"><svg width="47" height="47" viewBox="0 0 50 50"><path d="M22 16l9 9-9 9" stroke="#333" stroke-width="2" fill="none"/></svg></div>
</section>

<section class="patients">
  <svg width="0" height="0" style="position:absolute"><defs><path id="s" d="M9.5 0l2.9 6 6.6.8-4.9 4.5 1.3 6.5-5.9-3.3-5.9 3.3 1.3-6.5L0 6.8 6.6 6z"/></defs></svg>
  <div class="deco" role="img" aria-label="Illustration of a branch with a bee, bird and honeycomb" style="left:900px;top:0;width:300px;height:210px;background:radial-gradient(ellipse at 60% 45%,#a7d37b 0%,#d8ea9c 40%,rgba(255,255,255,0) 72%)"></div>
  <h2 class="section-title" style="top:78px">Our Happy Patients</h2>
  <div class="review" style="left:100px">
    <svg width="105" height="19" viewBox="0 0 105 19"><g fill="#f5b400"><use href="#s"/><use href="#s" x="21.5"/><use href="#s" x="43"/><use href="#s" x="64.5"/><use href="#s" x="86"/></g></svg>
    <p>Sed ut perspiciatis unde ois iste natus error sit vm accusantium doloremque laudantium, tom rem aperiam, eaque ipsa quae ab illo inventore veritatis et quasi architecto</p>
    <div class="who"><span class="av" role="img" aria-label="Patient photo"></span>- Alex Carter</div>
  </div>
  <div class="review" style="left:445px">
    <svg width="105" height="19" viewBox="0 0 105 19"><g fill="#f5b400"><use href="#s"/><use href="#s" x="21.5"/><use href="#s" x="43"/><use href="#s" x="64.5"/><use href="#s" x="86"/></g></svg>
    <p>Sed ut perspiciatis unde ois iste natus error sit vm accusantium doloremque laudantium, tom rem aperiam, eaque ipsa quae ab illo inventore veritatis et quasi architecto</p>
    <div class="who"><span class="av" role="img" aria-label="Patient photo"></span>- Alex Carter</div>
  </div>
  <div class="review" style="left:790px">
    <svg width="105" height="19" viewBox="0 0 105 19"><g fill="#f5b400"><use href="#s"/><use href="#s" x="21.5"/><use href="#s" x="43"/><use href="#s" x="64.5"/><use href="#s" x="86"/></g></svg>
    <p>Sed ut perspiciatis unde ois iste natus error sit vm accusantium doloremque laudantium, tom rem aperiam, eaque ipsa quae ab illo inventore veritatis et quasi architecto</p>
    <div class="who"><span class="av" role="img" aria-label="Patient photo"></span>- Alex Carter</div>
  </div>
</section>

<section class="contact">
  <div class="abs" style="left:1110px;top:0;width:110px;height:110px;border-radius:50%;background:#cdeccb"></div>
  <div class="abs" style="left:86px;top:492px;width:26px;height:26px;border-radius:50%;background:#cdeccb"></div>
  <div class="map" role="img" aria-label="Street map showing the practice location"></div>
  <div class="soc-row"><span class="soc"></span><span class="soc"></span><span class="soc"></span></div>
  <div class="info">
    <h4>Our Phone</h4>
    <div class="val"><svg width="11" height="11" viewBox="0 0 24 24"><rect x="1" y="1" width="22" height="22" rx="4" fill="#3d9a54"/><path d="M8 5c1 0 2 3 2 4s-2 1-1 3 2 3 3 3 1-1 2-1 4 1 4 2-1 3-3 3C10 19 5 14 5 8c0-2 2-3 3-3z" fill="#fff"/></svg>+1 (555) 010 2040</div>
    <h4>Address</h4>
    <div class="val"><svg width="9" height="12" viewBox="0 0 9 12"><path d="M4.5 0C2 0 0 2 0 4.5 0 8 4.5 12 4.5 12S9 8 9 4.5C9 2 7 0 4.5 0z" fill="#3d9a54"/><circle cx="4.5" cy="4.5" r="1.6" fill="#fff"/></svg>48 Orchard Lane&nbsp; Springfield USA 20410</div>
    <h4 style="border:0;margin-bottom:0">Pediatric Dentistry Hours</h4>
    <table class="hours">
      <tr><td>Monday</td><td>7:00am to 6:00pm</td></tr>
      <tr><td>Tuesday</td><td>7:00am to 6:00pm</td></tr>
      <tr><td>Wednesday</td><td>7:00am to 6:00pm</td></tr>
      <tr><td>Thursday</td><td>7:00am to 6:00pm</td></tr>
      <tr><td style="border:0">Friday</td><td style="border:0">7:00am to 3:00pm</td></tr>
    </table>
  </div>
  <div class="form">
    <div class="field">Name</div>
    <div class="field">Mobile Phone</div>
    <div class="field">Email</div>
    <div class="field msg">Message</div>
    <span class="btn btn-green">Submit <span class="arr"></span></span>
  </div>
</section>

<footer class="site-footer">
  <div class="foot-brand"><span class="brand-dot"></span><span class="brand-name">birchwood</span></div>
  <div class="foot-nav"><span>Home</span><i>|</i><span>About Us</span><i>|</i><span>New patients</span><i>|</i><span>Dentistry</span><i>|</i><span>Forms</span><i>|</i><span>Contact Us</span></div>
  <div class="copy">© Copyright 2021 Birchwood pediatric dentistry. All rights reserved.</div>
  <div class="foot-soc"><span></span><span></span><span></span><span></span></div>
</footer>

</body>
</html>
```